Construction machinery rental / heavy equipment rental needs a nice billboard

We need a billboard for our company.
We rent out construction machinery such as excavators, wheel loaders, wheel dumpers and so on...

I would like an elegant, simple, dark design.
Colors: black yellow grey white

The following must be on the billboard:
Logo
phone number: 078 / 513 90 41
website: www.kiesgrube-talwerk.ch
the machines I rent out: Bagger bis 10T, Radlader, Dumper, Raupenkipper

the font in the logo is: Square 721

Final format 2950 x 1900mm
I have uploaded pictures:
"Excavator 1-6" are my pictures, which can be used
"Sample 1-4" are pictures whose style I like
"Billboard" are billboards which I like

Requirements
Must have
• The following must be on the billboard: Logo phone number: 078 / 513 90 41 website: www.kiesgrube-talwerk.ch the machines I rent out: Bagger bis 10T, Radlader, Dumper, Raupenkipper

```html
<!DOCTYPE html>
<html lang="de">
<head>
<meta charset="utf-8">
<title>Talwerk Baumaschinenvermietung – Banner</title>
<link rel="stylesheet" href="https://fonts.googleapis.com/css2?family=Open+Sans:ital,wdth,wght@0,75..100,400..800;1,75..100,400..800&display=swap">
<style>
  :root {
    --stage: #8e8f93;
    --black: #050505;
    --yellow: #b9a30c;
    --yellow-dark: #8f7e12;
    --grey-light: #d9dadc;
    --grey-mid: #a7a9ac;
    --white: #f2f2f2;
    --text-grey: #c4c4c4;
  }
  * { margin: 0; padding: 0; box-sizing: border-box; }
  html, body { width: 1200px; height: 881px; overflow: hidden; }
  body { background: var(--stage); font-family: "Open Sans", sans-serif; position: relative; }

  .banner { position: absolute; top: 216px; height: 485px; background: var(--black); overflow: hidden; }
  .banner--wide { left: 107px; width: 693px; }
  .banner--tall { left: 854px; width: 241px; }

  .photo { position: absolute; }
  .banner--wide .photo-main {
    left: 150px; top: 40px; width: 543px; height: 445px;
    background:
      radial-gradient(ellipse 60px 40px at 62% 88%, rgba(255,255,255,0.55), transparent 70%),
      radial-gradient(ellipse 90px 60px at 86% 50%, rgba(230,230,230,0.55), transparent 70%),
      radial-gradient(ellipse 140px 110px at 78% 38%, rgba(150,150,150,0.6), transparent 75%),
      radial-gradient(ellipse 260px 90px at 50% 88%, rgba(70,70,70,0.8), transparent 80%),
      radial-gradient(ellipse 300px 240px at 68% 45%, #555 0%, #2a2a2a 45%, #111 75%, transparent 100%),
      linear-gradient(90deg, transparent 0%, #0b0b0b 30%, #151515 100%);
  }

  .logo { position: absolute; display: flex; flex-direction: column; align-items: flex-start; }
  .logo-row { display: flex; align-items: center; gap: 5px; }
  .logo-mark { background: var(--yellow); }
  .logo-name { color: var(--yellow); font-weight: 800; line-height: 1; letter-spacing: 0.02em; }
  .logo-sub { color: var(--white); font-weight: 600; letter-spacing: 0.04em; line-height: 1; margin-top: 2px; }

  .banner--wide .logo { left: 480px; top: 27px; }
  .banner--wide .logo-mark { width: 22px; height: 22px; }
  .banner--wide .logo-name { font-size: 28px; }
  .banner--wide .logo-sub { font-size: 7px; }

  .headline { position: absolute; line-height: 1; }
  .headline-top { color: var(--white); font-weight: 500; display: block; }
  .headline-main { color: var(--yellow); font-weight: 800; display: block; }
  .banner--wide .headline { left: 42px; top: 62px; }
  .banner--wide .headline-top { font-size: 50px; margin-left: 4px; }
  .banner--wide .headline-main { font-size: 80px; margin-top: -4px; }

  .machines { position: absolute; list-style: none; }
  .machine {
    position: absolute; left: 0; display: flex; align-items: center;
    font-style: italic; font-stretch: 92%; font-weight: 500; color: var(--black);
    clip-path: polygon(0 0, 100% 0, calc(100% - var(--cut)) 100%, 0 100%);
  }
  .machine--grey { background: linear-gradient(90deg, var(--grey-mid), var(--grey-light) 40%, var(--grey-mid)); }
  .machine--yellow { background: linear-gradient(90deg, var(--yellow), var(--yellow-dark)); }

  .banner--wide .machines { left: 32px; top: 207px; }
  .banner--wide .machine { height: 28px; padding-left: 27px; font-size: 21px; --cut: 16px; }

  .phone-band {
    position: absolute; left: 0; background: var(--yellow);
    clip-path: polygon(0 0, 100% 0, calc(100% - var(--cut)) 100%, 0 100%);
    display: flex; align-items: center;
  }
  .phone { color: var(--black); font-weight: 800; font-stretch: 90%; line-height: 1; }
  .banner--wide .phone-band { top: 372px; width: 387px; height: 51px; --cut: 38px; padding-left: 32px; }
  .banner--wide .phone { font-size: 45px; }

  .stripes { position: absolute; }
  .banner--wide .stripes { left: 368px; top: 372px; width: 92px; height: 51px; }

  .website { position: absolute; color: var(--text-grey); font-style: italic; font-weight: 600; letter-spacing: 0.34em; white-space: nowrap; }
  .banner--wide .website { left: 36px; top: 429px; font-size: 15px; }

  .feature-ring {
    position: absolute; left: 470px; top: 270px; width: 194px; height: 194px; border-radius: 50%;
    background: #0c0c0c; border: 5px solid #1a1a1a;
    box-shadow: inset 0 0 0 3px var(--yellow), inset 0 0 0 7px #9a9a9a;
    display: flex; align-items: center; justify-content: center;
  }
  .feature-photo {
    width: 166px; height: 166px; border-radius: 50%;
    background:
      radial-gradient(ellipse 22px 8px at 62% 50%, rgba(190,210,255,0.8), transparent 75%),
      radial-gradient(ellipse 70px 45px at 55% 55%, #3a3a3e, transparent 80%),
      radial-gradient(ellipse 90px 18px at 50% 88%, rgba(80,80,85,0.7), transparent 80%),
      radial-gradient(circle at 50% 45%, #1c1c1f 0%, #0a0a0a 70%, #040404 100%);
  }

  /* tall banner */
  .banner--tall .logo { left: 48px; top: 30px; }
  .banner--tall .logo-mark { width: 18px; height: 18px; }
  .banner--tall .logo-name { font-size: 22px; }
  .banner--tall .logo-sub { font-size: 5.5px; }

  .rule { position: absolute; left: 0; width: 100%; height: 3px; background: var(--yellow); }
  .banner--tall .photo-top {
    left: 0; top: 89px; width: 100%; height: 171px;
    background:
      radial-gradient(ellipse 24px 16px at 86% 58%, rgba(255,255,255,0.9), transparent 75%),
      radial-gradient(ellipse 14px 10px at 73% 62%, rgba(230,90,60,0.7), transparent 75%),
      radial-gradient(ellipse 60px 40px at 80% 40%, rgba(120,130,150,0.45), transparent 80%),
      radial-gradient(ellipse 140px 60px at 55% 92%, #5a4634, transparent 80%),
      linear-gradient(180deg, #070707 0%, #141414 45%, #2a2119 80%, #3a2e22 100%);
  }
  .banner--tall .photo-bottom {
    left: 0; top: 263px; width: 100%; height: 222px;
    background:
      radial-gradient(ellipse 120px 180px at 95% 40%, #2f2f2f 0%, #181818 50%, transparent 85%),
      radial-gradient(ellipse 200px 60px at 60% 100%, #222, transparent 80%),
      var(--black);
  }
  .banner--tall .headline { left: 20px; top: 279px; }
  .banner--tall .headline-top { font-size: 22px; margin-left: 2px; }
  .banner--tall .headline-main { font-size: 38px; margin-top: -2px; }

  .banner--tall .machines { left: 16px; top: 347px; }
  .banner--tall .machine { height: 13px; padding-left: 13px; font-size: 10.5px; --cut: 8px; }

  .banner--tall .phone-band { top: 427px; width: 186px; height: 24px; --cut: 18px; padding-left: 16px; }
  .banner--tall .phone { font-size: 22px; }
  .banner--tall .stripes { left: 178px; top: 427px; width: 44px; height: 24px; }
  .banner--tall .website { left: 17px; top: 453px; font-size: 8px; letter-spacing: 0.3em; }
</style>
</head>
<body>

<section class="banner banner--wide" aria-label="Querbanner">
  <div class="photo photo-main" role="img" aria-label="Nachtaufnahme eines Minibaggers bei der Arbeit, im Scheinwerferlicht"></div>

  <div class="logo">
    <div class="logo-row"><span class="logo-mark"></span><span class="logo-name">TALWERK</span></div>
    <span class="logo-sub">BAUMASCHINENVERMIETUNG</span>
  </div>

  <h1 class="headline">
    <span class="headline-top">The Machines</span>
    <span class="headline-main">I Rent Out</span>
  </h1>

  <ul class="machines">
    <li class="machine machine--grey" style="top:0;width:272px">• BAGGER BIS 10T</li>
    <li class="machine machine--yellow" style="top:39px;width:203px">• RADLADER</li>
    <li class="machine machine--grey" style="top:78px;width:163px">• DUMPER</li>
    <li class="machine machine--yellow" style="top:118px;width:203px">• RAUPENKIPPER</li>
  </ul>

  <div class="phone-band"><span class="phone">078 / 513 90 41</span></div>
  <svg class="stripes" viewBox="0 0 92 51" aria-hidden="true">
    <polygon points="28,0 36,0 8,51 0,51" fill="#d0d0d0"/>
    <polygon points="53,0 61,0 33,51 25,51" fill="#d0d0d0"/>
    <polygon points="78,0 86,0 58,51 50,51" fill="#d0d0d0"/>
  </svg>

  <p class="website">www.kiesgrube-talwerk.ch</p>

  <div class="feature-ring">
    <div class="feature-photo" role="img" aria-label="Schwarzer Sportwagen im Dunkeln mit leuchtenden Scheinwerfern"></div>
  </div>
</section>

<section class="banner banner--tall" aria-label="Rollup-Banner">
  <div class="logo">
    <div class="logo-row"><span class="logo-mark"></span><span class="logo-name">TALWERK</span></div>
    <span class="logo-sub">BAUMASCHINENVERMIETUNG</span>
  </div>

  <div class="rule" style="top:86px"></div>
  <div class="photo photo-top" role="img" aria-label="Minibagger bei Nacht mit Scheinwerfern auf einer Baustelle"></div>
  <div class="rule" style="top:260px"></div>
  <div class="photo photo-bottom" role="img" aria-label="Abgedunkelter Baggerarm im Hintergrund"></div>

  <h2 class="headline">
    <span class="headline-top">The Machines</span>
    <span class="headline-main">I Rent Out</span>
  </h2>

  <ul class="machines">
    <li class="machine machine--grey" style="top:0;width:131px">• BAGGER BIS 10T</li>
    <li class="machine machine--yellow" style="top:19px;width:98px">• RADLADER</li>
    <li class="machine machine--grey" style="top:38px;width:78px">• DUMPER</li>
    <li class="machine machine--yellow" style="top:57px;width:98px">• RAUPENKIPPER</li>
  </ul>

  <div class="phone-band"><span class="phone">078 / 513 90 41</span></div>
  <svg class="stripes" viewBox="0 0 44 24" aria-hidden="true">
    <polygon points="13,0 17,0 4,24 0,24" fill="#d0d0d0"/>
    <polygon points="26,0 30,0 17,24 13,24" fill="#d0d0d0"/>
    <polygon points="39,0 43,0 30,24 26,24" fill="#d0d0d0"/>
  </svg>

  <p class="website">www.kiesgrube-talwerk.ch</p>
</section>

</body>
</html>
```